Velmora Grove Club Postcard Design

Need a postcard for this business. Go to velmoragroveclub.com to see the product we are selling. Here's another good postcard you can sample. https://www.rowanpilsbydesign.com/?lightbox=dataItem-qz4tunal
Another one: http://blog.tranquet.com/postcard-examples-from-popular-startups/

```html
<!DOCTYPE html>
<html lang="en">
<head>
<meta charset="utf-8">
<title>Velmora Grove Club Postcard</title>
<link href="https://fonts.googleapis.com/css2?family=Oswald:wght@600&family=Montserrat:wght@400;700;900&family=Josefin+Slab:wght@600&display=swap" rel="stylesheet">
<style>
  :root {
    --page-bg: #e7e4df;
    --card-bg: #f4f4f4;
    --ink: #333333;
    --green: #7cc242;
    --bar: #414141;
    --panel: #ebebeb;
    --white: #ffffff;
  }
  * { box-sizing: border-box; margin: 0; padding: 0; }
  html, body { width: 1200px; height: 1011px; overflow: hidden; }
  body { background: var(--page-bg); position: relative; font-family: "Montserrat", sans-serif; }

  .postcard {
    position: absolute; left: 50px; top: 146px;
    width: 1100px; height: 718px;
    background: var(--card-bg);
    overflow: hidden;
    box-shadow: 0 6px 24px rgba(0,0,0,.18);
  }

  .offer-banner {
    position: absolute; left: 71px; top: 65px; width: 574px; height: 80px;
    background: var(--green);
    clip-path: polygon(0 0, 100% 0, 98% 50%, 100% 100%, 0 100%, 2% 50%);
    display: flex; align-items: center; justify-content: center;
    font-family: "Oswald", sans-serif; font-weight: 600; font-size: 42px;
    color: var(--white); letter-spacing: .5px;
  }
  .offer-banner sup { font-size: 22px; position: relative; top: -4px; }

  .headline {
    position: absolute; left: 78px; top: 168px;
    font-weight: 900; font-size: 106px; line-height: 1; color: var(--ink);
    letter-spacing: -3px; white-space: nowrap;
  }
  .headline .discount { color: var(--green); }

  .subhead {
    position: absolute; left: 83px; top: 280px;
    font-weight: 400; font-size: 34px; line-height: 40px; letter-spacing: 7.6px; color: #222;
    white-space: nowrap;
  }

  .how-it-works {
    position: absolute; left: 58px; top: 357px; width: 617px; height: 208px;
    background: var(--panel);
  }
  .how-it-works__title {
    position: absolute; top: 22px; left: 0; width: 100%;
    display: flex; align-items: center; justify-content: center; gap: 30px;
    font-weight: 700; font-size: 25px; color: #222;
  }
  .how-it-works__title::before,
  .how-it-works__title::after {
    content: ""; width: 118px; height: 2px; background: var(--green);
  }
  .steps { position: absolute; top: 72px; left: 0; width: 100%; display: flex; }
  .step {
    flex: 1; display: flex; flex-direction: column; align-items: center;
    border-left: 1px solid #cfcfcf;
  }
  .step:first-child { border-left: none; }
  .step__art { width: 70px; height: 58px; border-radius: 6px; }
  .step__art--dog { background: linear-gradient(135deg, #fff, #b25a3a); }
  .step__art--cattle { background: linear-gradient(135deg, #1f1f1f, #444); width: 84px; }
  .step__art--parcel { background: linear-gradient(135deg, #e3b96b, #b88a3e); width: 66px; }
  .step__label {
    margin-top: 10px; font-family: "Josefin Slab", serif; font-weight: 600;
    font-size: 22px; line-height: 26px; text-align: center; color: #222;
  }

  .code-bar {
    position: absolute; left: 0; top: 621px; width: 100%; height: 97px;
    background: var(--bar);
  }
  .code-bar__text {
    position: absolute; left: 362px; top: 22px; width: 400px; text-align: center;
    color: var(--white); font-weight: 400;
  }
  .code-bar__line1 { font-size: 24px; letter-spacing: .8px; white-space: nowrap; }
  .code-bar__line1 strong { color: var(--green); font-weight: 700; }
  .code-bar__line2 { font-size: 20px; letter-spacing: 1px; margin-top: 6px; }

  .join-button {
    position: absolute; left: 58px; top: 598px; width: 304px; height: 70px;
    background: var(--green); border: 3px solid var(--white);
    transform: rotate(-2deg);
    display: flex; align-items: center; justify-content: center;
    color: var(--white); font-weight: 900; font-size: 29px;
  }

  .product-photo {
    position: absolute; left: 740px; top: 0; width: 360px; height: 436px;
    background: radial-gradient(ellipse at 65% 45%, #c98d5e 0%, #a5764f 30%, #e9e2dc 70%, var(--card-bg) 100%);
  }

  .club-badge {
    position: absolute; left: 782px; top: 473px; width: 214px; height: 214px;
    border-radius: 50%; background: var(--white);
    box-shadow: 0 2px 8px rgba(0,0,0,.2);
    display: flex; align-items: center; justify-content: center; text-align: center;
    font-weight: 700; font-size: 22px; line-height: 28px; color: var(--ink);
    padding: 20px;
  }
</style>
</head>
<body>
  <main class="postcard">
    <div class="offer-banner">TRY YOUR 1<sup>st</sup>&nbsp;SUBSCRIPTION</div>

    <h1 class="headline">SAVE <span class="discount">50%</span></h1>
    <p class="subhead">ON YOUR FIRST MONTH</p>

    <section class="how-it-works">
      <h2 class="how-it-works__title">HOW IT WORKS</h2>
      <div class="steps">
        <div class="step">
          <div class="step__art step__art--dog" role="img" aria-label="Illustration of a happy small dog with a ribbon award"></div>
          <p class="step__label">Doggy joy<br>guarantee</p>
        </div>
        <div class="step">
          <div class="step__art step__art--cattle" role="img" aria-label="Silhouette of a cow marked premium quality"></div>
          <p class="step__label">Sourced from<br>free range cattle</p>
        </div>
        <div class="step">
          <div class="step__art step__art--parcel" role="img" aria-label="Illustration of a taped cardboard parcel"></div>
          <p class="step__label">Shipped to<br>your doorstep</p>
        </div>
      </div>
    </section>

    <div class="product-photo" role="img" aria-label="Photo of bully stick chews scattered beside a kraft mailer box"></div>

    <div class="code-bar">
      <div class="code-bar__text">
        <p class="code-bar__line1">USE CODE <strong>VELMORAGROVE</strong></p>
        <p class="code-bar__line2">AT CHECKOUT</p>
      </div>
    </div>

    <div class="join-button">JOIN THE CLUB</div>

    <div class="club-badge">Velmora Grove Club</div>
  </main>
</body>
</html>
```